Brand new website for global research and investment startup

We need a simple website, maybe 3 pages: landing page with business description, investment philosophy, team and contact info.
We have a logo already that can be incorporated. Please use the logo only, not the text
We like the color green, something along the lines of #3D6C32 as the main color.
We'd like to design the website with geometric shapes in gradations of the base color. The shapes should suggest "work in progress", "built to last (a long time)", "solidity" and "indestructibility". One idea floating in my head sees smaller features with icosahedron and dodecahedron shapes, and maybe larger structures like crystal lattices; but please feel free to be creative and imagine your own.

```html
<!DOCTYPE html>
<html lang="en">
<head>
<meta charset="utf-8">
<title>Stratum Capital — Built to Endure</title>
<link rel="stylesheet" href="https://fonts.googleapis.com/css2?family=Outfit:wght@300;400;500;600;700;800&display=swap">
<style>
:root{
  --green:#3D6C32;
  --green-dark:#1f4a24;
  --green-mid:#4a7f4e;
  --green-light:#7fbf78;
  --ink:#141414;
  --text:#3a3a3a;
  --card:#f0f0f0;
  --rule:#cfcfcf;
  --white:#ffffff;
}
*{margin:0;padding:0;box-sizing:border-box}
html,body{width:1200px;height:2708px;overflow:hidden;background:var(--white)}
body{position:relative;font-family:'Outfit',sans-serif;color:var(--ink)}
.abs{position:absolute}
a{color:inherit;text-decoration:none}

/* hero */
.hero{left:0;top:0;width:1200px;height:652px;background:linear-gradient(115deg,var(--green-dark) 0%,#2d5e30 50%,var(--green-mid) 100%);overflow:hidden}
.hero-art{left:660px;top:130px;width:520px;height:520px;background:radial-gradient(closest-side,rgba(143,207,136,.85) 0%,rgba(100,160,96,.6) 45%,rgba(74,127,78,0) 100%)}
.nav{left:94px;top:25px;width:1012px;height:85px;background:var(--white);border-radius:14px;z-index:2}
.brand{left:22px;top:28px;font-weight:700;font-size:22px;letter-spacing:-.5px;color:#4a4a4a}
.nav-links{right:0;top:0;height:85px;display:flex;align-items:center;gap:34px;padding-right:19px;font-size:10.5px;letter-spacing:-.2px}
.nav-links .active{position:relative}
.nav-links .active::after{content:"";position:absolute;left:0;right:0;bottom:-10px;height:2px;background:var(--green)}
.btn-solid{background:var(--green);color:var(--white);border-radius:8px;padding:13px 31px;font-weight:500}
.hero-rule{left:94px;top:241px;width:3px;height:245px;background:var(--white)}
.hero-title{left:115px;top:234px;color:var(--white);font-weight:800;font-size:52px;line-height:50px;letter-spacing:-2.5px}
.hero-lead{left:117px;top:394px;width:430px;color:var(--white);font-size:10.5px;line-height:16px;letter-spacing:-.2px}
.hero-btn{top:447px;height:40px;border-radius:8px;display:flex;align-items:center;justify-content:center;font-size:10.5px;font-weight:500;letter-spacing:-.2px}
.hero-btn.primary{left:117px;width:197px;background:var(--white);color:var(--ink)}
.hero-btn.ghost{left:320px;width:157px;border:1px solid var(--white);color:var(--white)}

/* overview */
.overview-art{left:195px;top:730px;width:325px;height:328px;background:linear-gradient(135deg,#a8e59c,#4f9a4c 60%,#3f7f3e);clip-path:polygon(30% 0,70% 2%,95% 28%,100% 60%,80% 92%,45% 100%,12% 82%,0 45%,10% 15%)}
.eyebrow{font-weight:700;font-size:15px;letter-spacing:-.4px}
.section-title{font-weight:700;font-size:32px;letter-spacing:-1.5px}
.underline{height:2px;width:34px;background:var(--green)}
.body-copy{font-size:10.5px;line-height:16px;color:var(--text);letter-spacing:-.2px}
.body-copy p+p{margin-top:10px}

/* pillars */
.center-title{left:0;width:1200px;text-align:center;font-weight:700;font-size:31px;letter-spacing:-1.5px}
.center-rule{left:573px;width:54px;height:2px;background:var(--green)}
.pillar{top:1202px;width:296px;height:211px;background:var(--card);border-radius:14px;text-align:center}
.pillar-icon{display:block;margin:27px auto 0;width:56px;height:64px;background:var(--green);clip-path:polygon(50% 0,100% 25%,100% 75%,50% 100%,0 75%,0 25%)}
.pillar h3{margin-top:18px;font-size:15px;font-weight:700;letter-spacing:-.5px}
.pillar p{margin:10px auto 0;width:235px;font-size:10px;line-height:16px;color:var(--text);letter-spacing:-.2px}

/* principles */
.principles-title{left:141px;top:1640px;font-weight:700;font-size:21px;letter-spacing:-1px}
.principle-list{left:141px;top:1685px;width:365px;list-style:none}
.principle{display:flex;align-items:center;gap:13px;height:83px;border-bottom:1px solid var(--rule);padding-bottom:12px}
.principle+.principle{padding-top:12px}
.principle:last-child{border-bottom:none}
.principle-icon{width:58px;height:58px;border-radius:50%;background:var(--green);display:flex;align-items:center;justify-content:center;flex:none}
.principle span{font-weight:700;font-size:15px;letter-spacing:-.5px}
.sphere-art{left:655px;top:1660px;width:345px;height:345px;border-radius:50%;background:radial-gradient(circle at 50% 30%,#a6dc9c 0%,#78b170 35%,#4f8a48 70%,#3b6f35 100%);box-shadow:0 18px 30px rgba(0,0,0,.08)}

/* cta + footer */
.cta{left:0;top:2112px;width:1200px;height:596px;background:linear-gradient(200deg,#72a268 0%,#4a833f 35%,#3b7134 100%);color:var(--white)}
.cta-brand{left:200px;top:110px;width:300px;text-align:center;font-weight:700;font-size:34px;letter-spacing:-1px}
.cta-eyebrow{left:577px;top:83px}
.cta-title{left:577px;top:110px;font-size:31px}
.cta-rule{left:577px;top:150px;background:var(--white)}
.cta-copy{left:577px;top:170px;font-size:10.5px;letter-spacing:-.2px}
.cta-btn{left:577px;top:198px;width:183px;height:38px;border:1px solid var(--white);border-radius:8px;display:flex;align-items:center;justify-content:center;font-size:10px;font-weight:500}
.footer-rule{left:94px;width:1012px;height:1px;background:rgba(255,255,255,.3)}
.footer-brand{left:0;top:395px;width:1200px;text-align:center;font-weight:700;font-size:28px;letter-spacing:-.8px}
.footer-links{left:390px;top:510px;font-size:12px;display:flex}
.footer-links a:nth-child(1){width:97px}
.footer-links a:nth-child(2){width:252px}
.copyright{left:0;top:572px;width:1200px;text-align:center;font-size:10px}
</style>
</head>
<body>

<header class="hero abs">
  <div class="hero-art abs" role="img" aria-label="Green crystal lattice polyhedron with floating geometric shards"></div>
  <nav class="nav abs">
    <div class="brand abs">Stratum Capital</div>
    <div class="nav-links abs">
      <a class="active">HOME</a>
      <a>INVESTMENT PHILOSOPHY &amp; TEAM</a>
      <a>CONTACT US</a>
      <a class="btn-solid">GET IN TOUCH</a>
    </div>
  </nav>
  <div class="hero-rule abs"></div>
  <h1 class="hero-title abs">BUILT TO<br>ENDURE. DESIGNED<br>FOR GROWTH.</h1>
  <p class="hero-lead abs">Constructing high-conviction portfolios grounded in structural stability, deep market insight, and long-term value creation.</p>
  <a class="hero-btn primary abs">OUR INVESTMENT STRATEGY</a>
  <a class="hero-btn ghost abs">CONTACT OUR TEAM</a>
</header>

<section>
  <div class="overview-art abs" role="img" aria-label="Faceted green polyhedron"></div>
  <div class="eyebrow abs" style="left:609px;top:773px">BUSINESS OVERVIEW</div>
  <h2 class="section-title abs" style="left:608px;top:797px">FOUNDATION &amp; PURPOSE</h2>
  <div class="underline abs" style="left:609px;top:841px"></div>
  <div class="body-copy abs" style="left:588px;top:868px;width:410px">
    <p>We are a forward-thinking investment firm dedicated to identifying, nurturing, and scaling high-potential opportunities across global markets. Our primary focus spans resilient real assets, durable business architectures, and transformative strategies explicitly engineered to withstand macroeconomic volatility and shifting market cycles.</p>
    <p>By combining rigorous analytical frameworks, deep risk discipline, and an active building mindset, we transform complex financial environments into structured, long-term performance. We do not simply allocate capital—we actively construct, optimize, and fortify strong foundational platforms designed to endure and deliver sustained value for generations to come.</p>
  </div>
</section>

<section>
  <h2 class="center-title abs" style="top:1126px">INVESTMENT PILLARS (PHILOSOPHY TEASER)</h2>
  <div class="center-rule abs" style="top:1175px"></div>
  <article class="pillar abs" style="left:144px">
    <span class="pillar-icon" role="img" aria-label="Icosahedron icon"></span>
    <h3>STRUCTURAL RESILIENCE</h3>
    <p>We prioritize fundamentals and robust asset architectures are built to resist market shifts and deliver durable capital preservation.</p>
  </article>
  <article class="pillar abs" style="left:453px">
    <span class="pillar-icon" role="img" aria-label="Icosahedron icon"></span>
    <h3>ACTIVE VALUE CREATION</h3>
    <p>Investing is not a static process. We treat capital as an active toolkit-continually optimizing, adapting, and growing our portfolio assets.</p>
  </article>
  <article class="pillar abs" style="left:761px">
    <span class="pillar-icon" role="img" aria-label="Icosahedron icon"></span>
    <h3>STRATEGIC LONGEVITY</h3>
    <p>Our horizon is measured in decades, not quarters. We back ideas and platforms engineered for lasting, generational impact.</p>
  </article>
</section>

<section>
  <h2 class="center-title abs" style="top:1493px">OUR BUSINESS FOUNDATION</h2>
  <div class="center-rule abs" style="top:1536px"></div>
  <p class="body-copy abs" style="left:280px;top:1554px;width:640px;text-align:center">We are a forward-thinking investment firm dedicated to identifying, nurturing, and scaling high-potential opportunities. Our focus spans resilient assets and transformative strategies designed to withstand economic volatility.</p>
  <h3 class="principles-title abs">KEY FIRM PRINCIPLES</h3>
  <ul class="principle-list abs">
    <li class="principle"><span class="principle-icon"><svg width="26" height="26" viewBox="0 0 26 26" fill="none" stroke="#fff" stroke-width="1.6"><circle cx="13" cy="11" r="7"/><path d="M3 22c4-3 16-3 20 0"/></svg></span><span>INVESTMENT DISCIPLINE</span></li>
    <li class="principle"><span class="principle-icon"><svg width="26" height="26" viewBox="0 0 26 26" fill="none" stroke="#fff" stroke-width="1.6"><circle cx="13" cy="13" r="9"/><path d="M4 13h18M13 4c4 5 4 13 0 18M13 4c-4 5-4 13 0 18"/></svg></span><span>GLOBAL INSIGHT</span></li>
    <li class="principle"><span class="principle-icon"><svg width="26" height="26" viewBox="0 0 26 26" fill="none" stroke="#fff" stroke-width="1.6"><rect x="4" y="9" width="11" height="8" rx="4" transform="rotate(-40 9 13)"/><rect x="11" y="9" width="11" height="8" rx="4" transform="rotate(-40 16 13)"/></svg></span><span>DURABLE STRUCTURES</span></li>
    <li class="principle"><span class="principle-icon"><svg width="26" height="26" viewBox="0 0 26 26" fill="none" stroke="#fff" stroke-width="1.6"><path d="M3 14l5-5 5 4 5-4 5 5-10 8z"/></svg></span><span>PARTNERSHIP FOCUSED</span></li>
  </ul>
  <div class="sphere-art abs" role="img" aria-label="Green faceted sphere wrapped in a network of connected nodes"></div>
</section>

<footer class="cta abs">
  <div class="cta-brand abs">Stratum Capital</div>
  <div class="eyebrow cta-eyebrow abs">CALL-TO-ACTION</div>
  <h2 class="section-title cta-title abs">READY TO BUILD TOGETHER?</h2>
  <div class="underline cta-rule abs"></div>
  <p class="cta-copy abs">Discover how our disciplined investment approach creates durable value for the long haul.</p>
  <a class="cta-btn abs">CONNECT WITH US TODAY</a>
  <div class="footer-rule abs" style="top:310px"></div>
  <div class="footer-brand abs">Stratum Capital</div>
  <nav class="footer-links abs"><a>HOME</a><a>INVESTMENT PHILOSOPHY &amp; TEAM</a><a>CONTACT US</a></nav>
  <div class="footer-rule abs" style="top:551px"></div>
  <p class="copyright abs">Copyright: © 2026 All Rights Reserved.</p>
</footer>

</body>
</html>
```